Massage Therapy and Personal Training Business Card (RT Restful)

I need a logo design based in Washington. The company is called RT Restful. RT are my initials. I specialize in massage therapy and personal training and general wellness of my clients. I've tried getting designs but haven't quite yet found what I'm looking for. I'm not inclined to a certain color yet but some color that resembles wellness such as light blue and white or green and white. Again, I'm not really picky about that. Thank you in advance

Industry/Entity Type

Business

Contact Information for Business Card

Have the description on one side and space for writing information on the back side such as number, appt, etc. I have an example attached. I see a lot of these card. I dont want the exact one, but something similar. Simple, professional and elegant.

Colors

Designer to choose colors to be used in the design.

Requirements
Must have
• Space on the back side to write
• A professional, elegant look
Should not have
• cartoon like style.

```html
<!DOCTYPE html>
<html lang="en">
<head>
<meta charset="utf-8">
<title>RT Restful – Business Card</title>
<link href="https://fonts.googleapis.com/css2?family=Quicksand:wght@500;600&family=Open+Sans:wght@400&display=swap" rel="stylesheet">
<style>
  :root {
    --backdrop: #ecebe8;
    --card: #ffffff;
    --card-fade: #ececec;
    --blue: #1aa6e4;
    --green: #6cbd45;
    --rule: #c9c9c9;
    --muscle-light: #d8d8d8;
    --muscle-dark: #8a8a8a;
  }
  html, body {
    margin: 0;
    padding: 0;
    width: 900px;
    height: 1200px;
    overflow: hidden;
    background: var(--backdrop);
  }
  .canvas {
    position: relative;
    width: 900px;
    height: 1200px;
  }
  .card {
    position: absolute;
    left: 92px;
    width: 716px;
    height: 418px;
    background: linear-gradient(to bottom, var(--card) 45%, var(--card-fade) 100%);
    box-shadow: 0 4px 14px rgba(0,0,0,0.18);
    overflow: hidden;
  }
  .card--front { top: 148px; }
  .card--back  { top: 633px; height: 419px; }

  .anatomy-art {
    position: absolute;
    left: 0; top: 0;
    width: 260px; height: 100%;
    background: linear-gradient(160deg, var(--muscle-light) 0%, var(--muscle-dark) 55%, var(--muscle-light) 100%);
  }

  .brand-name {
    position: absolute;
    font-family: "Quicksand", sans-serif;
    font-weight: 600;
    color: var(--blue);
    white-space: nowrap;
    display: flex;
    align-items: center;
    gap: 14px;
    margin: 0;
  }
  .brand-dot {
    width: 26px; height: 26px;
    border-radius: 50%;
    background: var(--green);
  }
  .card--front .brand-name { left: 306px; top: 88px; font-size: 46px; }
  .card--back .brand-name { left: 0; right: 0; justify-content: center; top: 45px; font-size: 40px; }

  .rule {
    position: absolute;
    height: 2px;
    background: var(--rule);
  }
  .rule--top { left: 308px; width: 368px; top: 219px; }
  .rule--mid { left: 308px; width: 368px; top: 318px; }
  .rule--full { left: 0; width: 100%; top: 142px; }

  .holder-name {
    position: absolute;
    left: 306px; top: 228px;
    margin: 0;
    font-family: "Quicksand", sans-serif;
    font-weight: 500;
    font-size: 31px;
    color: var(--blue);
  }
  .holder-role {
    position: absolute;
    left: 308px; top: 267px;
    margin: 0;
    font-family: "Open Sans", sans-serif;
    font-size: 15px;
    line-height: 21px;
    color: var(--green);
  }
  .contact {
    position: absolute;
    top: 328px;
    display: flex;
    align-items: center;
    gap: 6px;
    font-family: "Open Sans", sans-serif;
    font-size: 17px;
    color: var(--blue);
  }
  .contact--email { left: 308px; }
  .contact--phone { left: 522px; }
  .contact-icon { width: 30px; height: 30px; }

  .write-band {
    position: absolute;
    left: 0; bottom: 0;
    width: 100%; height: 18px;
    background: var(--green);
  }
</style>
</head>
<body>
<div class="canvas">

  <section class="card card--front">
    <div class="anatomy-art" role="img" aria-label="Anatomical illustration of a man's back muscles with shoulders and forearms highlighted in green"></div>

    <h1 class="brand-name"><span>RT Restful</span><span class="brand-dot"></span></h1>

    <div class="rule rule--top"></div>
    <h2 class="holder-name">Daniel Reyes</h2>
    <p class="holder-role">Massage therapy and personal training<br>general wellness</p>
    <div class="rule rule--mid"></div>

    <div class="contact contact--email">
      <svg class="contact-icon" viewBox="0 0 30 30" aria-hidden="true">
        <circle cx="15" cy="15" r="14" fill="#6cbd45" stroke="#d9efcf" stroke-width="2"/>
        <rect x="8" y="10" width="14" height="10" rx="1" fill="none" stroke="#fff" stroke-width="1.8"/>
        <polyline points="8,10.5 15,16 22,10.5" fill="none" stroke="#fff" stroke-width="1.8"/>
      </svg>
      <span>dan@rtrestful.com</span>
    </div>
    <div class="contact contact--phone">
      <svg class="contact-icon" viewBox="0 0 30 30" aria-hidden="true">
        <circle cx="15" cy="15" r="14" fill="#6cbd45" stroke="#d9efcf" stroke-width="2"/>
        <path d="M10.5 8.5c1-.6 1.8-.3 2.3.6l1 2c.3.7.1 1.3-.5 1.8l-.8.6c.7 1.6 1.9 2.9 3.5 3.6l.6-.8c.5-.6 1.2-.8 1.8-.5l2 1c.9.5 1.2 1.3.6 2.3-.8 1.3-2.2 1.9-3.7 1.4-4-1.3-7.1-4.4-8.4-8.4-.5-1.5.2-2.9 1.6-3.6z" fill="#fff"/>
      </svg>
      <span>801-555 0172</span>
    </div>
  </section>

  <section class="card card--back">
    <h1 class="brand-name"><span>RT Restful</span><span class="brand-dot"></span></h1>
    <div class="rule rule--full"></div>
    <div class="write-band"></div>
  </section>

</div>
</body>
</html>
```